Booth Design for our Brokerage division. We already have logos, color scheme and photos. The Brokerage division is called VelCargonix. This brokerage division is part of Steadfast Motor Carriers, Inc. A company that hauls automobiles. We are one of the leading finished vehicle logistics service providers in the United States serving all 48 states. We also provide transportation and logistical solutions for many new and used vehicle customers with our 3PL service division, VelCargonix. VelCargonix' services include storage, drive away, yard management, support for off rail movements, transportation of vehicles and many other solutions for your logistical needs.

We aren't set on the exact products, but I believe the booth size is 10 x 10. We were thinking about an 8' x 10' Backdrop and a 6 foot table wrap at least.

```html
<!DOCTYPE html>
<html lang="en">
<head>
<meta charset="utf-8">
<title>VelCargonix Booth – Backdrop and Table Wrap</title>
<link rel="stylesheet" href="https://fonts.googleapis.com/css2?family=Montserrat:wght@600;800;900&display=swap">
<style>
  :root {
    --brand-red: #e01b22;
    --deep-red: #a50f14;
    --ink: #111111;
    --white: #ffffff;
    --stage: #f3f3f3;
    --accent-yellow: #ffd21f;
    --tagline-blue: #1b3f9a;
  }
  * { box-sizing: border-box; margin: 0; padding: 0; }
  html, body { width: 1200px; height: 919px; overflow: hidden; }
  body {
    background: var(--stage);
    font-family: "Montserrat", Arial, sans-serif;
    position: relative;
  }

  /* ---------- Table wrap ---------- */
  .table-wrap {
    position: absolute; left: 100px; top: 430px;
    width: 290px; height: 370px;
    background: var(--white);
    overflow: hidden;
    box-shadow: 0 2px 10px rgba(0,0,0,.12);
  }
  .table-wrap .wrap-stripes { position: absolute; inset: 0; }
  .table-wrap .brand-name {
    position: absolute; left: 22px; top: 38px;
    font-weight: 900; font-size: 29px; color: var(--brand-red);
    letter-spacing: -0.5px;
  }
  .table-wrap .values { position: absolute; left: 22px; top: 92px; list-style: none; }
  .table-wrap .values li {
    font-weight: 800; font-size: 18px; color: var(--brand-red);
    width: 170px; padding-bottom: 3px; margin-bottom: 8px;
    border-bottom: 2px solid var(--brand-red); position: relative;
  }
  .table-wrap .values li::after {
    content: ""; position: absolute; right: -4px; bottom: -5px;
    width: 8px; height: 8px; border-radius: 50%; background: var(--brand-red);
  }
  .table-wrap .parent-name {
    position: absolute; left: 22px; top: 222px;
    font-weight: 800; font-size: 12px; color: var(--brand-red);
  }
  .table-wrap .phone {
    position: absolute; left: 22px; top: 268px;
    font-weight: 900; font-size: 21px; color: var(--ink);
  }
  .table-wrap .web {
    position: absolute; left: 22px; top: 298px;
    font-weight: 800; font-size: 12px; color: var(--brand-red);
  }

  /* ---------- Backdrop ---------- */
  .backdrop {
    position: absolute; left: 440px; top: 110px;
    width: 670px; height: 690px;
    background: var(--white);
    overflow: hidden;
    box-shadow: 0 2px 12px rgba(0,0,0,.14);
  }
  .backdrop .panel-shapes { position: absolute; inset: 0; }
  .backdrop .brand-name {
    position: absolute; left: 34px; top: 78px;
    font-weight: 900; font-size: 28px; color: var(--brand-red);
  }
  .backdrop .headline {
    position: absolute; left: 34px; top: 135px;
    font-weight: 900; font-size: 24px; line-height: 1.15;
    color: var(--white); text-transform: uppercase;
  }
  .backdrop .headline .accent { color: var(--brand-red); }
  .backdrop .services { position: absolute; left: 34px; top: 268px; list-style: none; }
  .backdrop .services li {
    font-weight: 800; font-size: 12.5px; line-height: 1.25;
    color: var(--white); text-transform: uppercase;
    margin-bottom: 12px; padding-left: 22px; position: relative; width: 210px;
  }
  .backdrop .services li::before {
    content: "»"; position: absolute; left: 0; top: -4px;
    color: var(--accent-yellow); font-size: 19px; font-weight: 900;
  }
  .backdrop .quote-button {
    position: absolute; left: 34px; top: 530px;
    background: var(--brand-red); color: var(--white);
    font-weight: 800; font-size: 11px; padding: 4px 10px; text-transform: uppercase;
  }
  .backdrop .phone {
    position: absolute; left: 34px; top: 556px;
    font-weight: 900; font-size: 24px; color: var(--white);
  }
  .backdrop .web {
    position: absolute; left: 34px; top: 589px;
    font-weight: 800; font-size: 12px; color: var(--accent-yellow);
  }
  .backdrop .closing-line {
    position: absolute; left: 34px; top: 622px;
    font-weight: 800; font-size: 10px; line-height: 1.35;
    color: var(--brand-red); text-transform: uppercase;
  }
  .backdrop .parent-name {
    position: absolute; right: 30px; top: 42px;
    font-weight: 800; font-size: 13px; color: var(--brand-red);
  }
  .backdrop .photo {
    position: absolute; border: 4px solid var(--white);
    box-shadow: 0 1px 4px rgba(0,0,0,.25);
  }
  .backdrop .photo-trailer-yard {
    left: 460px; top: 72px; width: 180px; height: 110px;
    background: linear-gradient(180deg, #b8c7d4 0%, #dfe5ea 55%, #7f8a93 100%);
  }
  .backdrop .photo-car-hauler {
    left: 460px; top: 194px; width: 180px; height: 100px;
    background: linear-gradient(180deg, #7fb1de 0%, #b8d3ea 50%, #8c3a3a 100%);
  }
  .backdrop .states-badge {
    position: absolute; left: 362px; top: 195px;
    width: 88px; height: 88px; border-radius: 50%;
    background: var(--white); border: 4px solid var(--tagline-blue);
    box-shadow: 0 0 0 3px var(--white), 0 0 0 5px var(--brand-red);
  }
  .backdrop .tagline {
    position: absolute; right: 26px; top: 320px;
    font-weight: 800; font-size: 12.5px; color: var(--tagline-blue);
    white-space: nowrap;
  }
  .backdrop .tagline .dot { color: var(--brand-red); margin: 0 4px; }
  .backdrop .photo-loaded-hauler {
    position: absolute; left: 265px; top: 355px; width: 405px; height: 335px;
    background: linear-gradient(180deg, #dfe6ec 0%, #c9ced3 35%, #b51d22 70%, #5d6a4a 100%);
    clip-path: polygon(16% 0, 100% 0, 100% 100%, 0 100%);
  }
</style>
</head>
<body>

  <section class="table-wrap" aria-label="Table wrap">
    <svg class="wrap-stripes" width="290" height="370" viewBox="0 0 290 370" aria-hidden="true">
      <polygon points="290,40 290,370 150,370" fill="var(--ink)"/>
      <polygon points="255,90 290,70 290,370 190,370" fill="var(--brand-red)"/>
      <polygon points="238,150 252,142 170,370 156,370" fill="var(--brand-red)"/>
      <polygon points="290,180 290,370 245,370" fill="var(--deep-red)"/>
    </svg>
    <div class="brand-name">VelCargonix</div>
    <ul class="values">
      <li>QUALITY</li>
      <li>EXCELLENCE</li>
      <li>INTEGRITY</li>
    </ul>
    <div class="parent-name">Steadfast Motor Carriers</div>
    <div class="phone">555 301 4820</div>
    <div class="web">VELCARGONIX.COM</div>
  </section>

  <section class="backdrop" aria-label="Backdrop">
    <svg class="panel-shapes" width="670" height="690" viewBox="0 0 670 690" aria-hidden="true">
      <polygon points="0,0 370,0 250,690 0,690" fill="var(--ink)"/>
      <polygon points="370,0 415,0 295,690 250,690" fill="var(--brand-red)"/>
      <polygon points="428,0 442,0 322,690 308,690" fill="var(--brand-red)"/>
      <polygon points="318,0 352,0 318,230 284,230" fill="var(--deep-red)"/>
      <polygon points="232,430 262,430 224,690 194,690" fill="var(--brand-red)"/>
      <polygon points="190,600 255,600 240,690 175,690" fill="var(--deep-red)"/>
    </svg>

    <div class="brand-name">VelCargonix</div>
    <h1 class="headline">Transportation<br><span class="accent">and</span> Logistical<br>Solutions</h1>
    <ul class="services">
      <li>Storage</li>
      <li>Drive Away</li>
      <li>Yard Management</li>
      <li>Supports Off Rail Movements</li>
      <li>Transportation of Vehicles</li>
    </ul>
    <div class="quote-button">Get a quote today !!</div>
    <div class="phone">555 301 4820</div>
    <div class="web">VELCARGONIX.COM</div>
    <p class="closing-line">Many solutions for<br>your logistical needs</p>

    <div class="parent-name">Steadfast Motor Carriers</div>
    <div class="photo photo-trailer-yard" role="img" aria-label="Photo of a white truck and enclosed trailer parked in a wet yard"></div>
    <div class="photo photo-car-hauler" role="img" aria-label="Photo of a red car hauler truck on the highway under blue sky"></div>
    <div class="states-badge" role="img" aria-label="Badge for serving all 48 states"></div>
    <div class="tagline"><span class="dot">•</span>QUALITY<span class="dot">•</span>EXCELLENCE<span class="dot">•</span>INTEGRITY</div>
    <div class="photo-loaded-hauler" role="img" aria-label="Photo of a red car hauler loaded with white SUVs"></div>
  </section>

</body>
</html>
```